Worrunga Contracting Pty Ltd.

We need a corporate brand/logo for a new company. The company is represented by Indigenous Australians in Western Australias far north West. The aea is the Kimberley. The work we are involved in is contracting our services to companies. Our services range from heavy earth working machinary to landscape rehabilitation including revegetation. Other services we provide are demolition, contaminated sites and water management. We are essentially a services provider for hire. We tender mostly for contracts wit hmining companies.

```html
<!DOCTYPE html>
<html lang="en">
<head>
<meta charset="utf-8">
<title>Worrunga Contracting – Business Cards</title>
<link href="https://fonts.googleapis.com/css2?family=Roboto:wght@400;500;700&display=swap" rel="stylesheet">
<style>
  :root {
    --backdrop: #d6d6d6;
    --card: #ffffff;
    --ink: #2b2b2b;
    --ink-soft: #3a3a3a;
    --accent: #e07b24;
    --accent-red: #c0392b;
    --rule: #9a9a9a;
    --faint-ring: #f1ece6;
  }
  * { margin: 0; padding: 0; box-sizing: border-box; }
  html, body {
    width: 1200px; height: 800px; overflow: hidden;
    background: var(--backdrop);
    font-family: "Roboto", Arial, sans-serif;
    color: var(--ink);
  }
  .card {
    position: absolute;
    top: 283px;
    width: 430px; height: 238px;
    background: var(--card);
    overflow: hidden;
  }
  .card--front { left: 110px; }
  .card--back { left: 637px; }

  /* Front card */
  .front-mark {
    position: absolute; left: 68px; top: 62px;
    width: 108px; text-align: center;
  }
  .front-mark__dot {
    width: 68px; height: 68px; border-radius: 50%;
    background: var(--accent); margin: 0 auto 10px;
  }
  .front-mark__name {
    font-size: 12px; font-weight: 700; letter-spacing: 1px; color: var(--ink);
  }
  .front-divider {
    position: absolute; left: 187px; top: 67px;
    width: 1px; height: 103px; background: var(--rule);
  }
  .contact-block { position: absolute; left: 200px; top: 64px; }
  .contact-block__name { font-size: 12.5px; font-weight: 500; line-height: 15px; }
  .contact-block__role { font-size: 9.5px; color: var(--accent-red); line-height: 12px; margin-bottom: 8px; }
  .contact-block__address { font-size: 9.5px; line-height: 14px; color: var(--ink-soft); margin-bottom: 7px; }
  .contact-list { list-style: none; }
  .contact-list li {
    display: flex; align-items: center; gap: 6px;
    font-size: 9.5px; line-height: 14.5px; color: var(--ink-soft);
  }
  .contact-list svg { width: 10px; height: 10px; flex: none; }
  .decor-ring {
    position: absolute; left: 266px; top: 86px;
    width: 200px; height: 200px; border-radius: 50%;
    background: radial-gradient(circle, #f3f3f3 0%, var(--faint-ring) 70%, rgba(241,236,230,0) 72%);
  }

  /* Back card */
  .lockup {
    position: absolute; left: 90px; top: 82px;
    display: flex; align-items: center;
  }
  .lockup__dot {
    width: 76px; height: 76px; border-radius: 50%;
    background: var(--accent);
  }
  .lockup__divider {
    width: 1px; height: 40px; background: var(--rule); margin: 0 9px 0 7px;
  }
  .lockup__text { color: var(--ink); font-weight: 700; }
  .lockup__name { font-size: 23px; letter-spacing: 0.5px; line-height: 24px; }
  .lockup__tag { font-size: 11.5px; letter-spacing: 0.4px; line-height: 14px; }
</style>
</head>
<body>

<section class="card card--front" aria-label="Business card front">
  <div class="decor-ring" role="img" aria-label="Faint circular decoration in warm neutral tones"></div>

  <div class="front-mark">
    <div class="front-mark__dot"></div>
    <div class="front-mark__name">WORRUNGA</div>
  </div>

  <div class="front-divider"></div>

  <div class="contact-block">
    <p class="contact-block__name">Daniel Hartley</p>
    <p class="contact-block__role">Director</p>
    <p class="contact-block__address">PO Box 3175<br>Cottesloe WA 6011</p>
    <ul class="contact-list">
      <li>
        <svg viewBox="0 0 10 10" aria-hidden="true"><circle cx="5" cy="5" r="5" fill="#c0392b"/><path d="M3.3 2.6c.3-.2.6 0 .7.3l.3.7c.1.2 0 .4-.2.5l-.3.2c.3.7.8 1.2 1.5 1.5l.2-.3c.1-.2.3-.3.5-.2l.7.3c.3.1.5.4.3.7l-.3.5c-.2.3-.6.4-.9.3C4.6 6.8 3.2 5.4 2.8 4.1c-.1-.3 0-.7.3-.9z" fill="#fff"/></svg>
        +61 412 555 017
      </li>
      <li>
        <svg viewBox="0 0 10 10" aria-hidden="true"><circle cx="5" cy="5" r="5" fill="#c0392b"/><rect x="2.6" y="3.3" width="4.8" height="3.4" rx=".4" fill="#fff"/><path d="M2.8 3.5 5 5.2l2.2-1.7" fill="none" stroke="#c0392b" stroke-width=".6"/></svg>
        dan@worrungacontracting.com.au
      </li>
      <li>
        <svg viewBox="0 0 10 10" aria-hidden="true"><circle cx="5" cy="5" r="5" fill="#c0392b"/><circle cx="5" cy="5" r="2.4" fill="none" stroke="#fff" stroke-width=".6"/><path d="M2.6 5h4.8M5 2.6c-1.1 1.3-1.1 3.5 0 4.8M5 2.6c1.1 1.3 1.1 3.5 0 4.8" fill="none" stroke="#fff" stroke-width=".5"/></svg>
        www.worrungacontracting.com.au
      </li>
    </ul>
  </div>
</section>

<section class="card card--back" aria-label="Business card back">
  <div class="lockup">
    <div class="lockup__dot"></div>
    <div class="lockup__divider"></div>
    <div class="lockup__text">
      <p class="lockup__name">WORRUNGA</p>
      <p class="lockup__tag">CONTRACTING PTY LTD</p>
    </div>
  </div>
</section>

</body>
</html>
```